Fire and Building compliance company needs website

A professional website is needed for Pembury Alarm Group 2019 , company profile attached- we have a website but it is old and needs replacing (in fact we can not access it at present).

We are also looking at getting logo redesigned and will probably change to a flame type graphic with the letters PAG and then Fire and Building Compliance (bellow PAG).

• Ease of use
Page should fit inside typical screen size (not have to scroll down to see page).
Be made in Joomla 2.5

search words- Wanganui, fire alarm, building compliance, building warrant of fitness,BWOF, burglar alarm systems, LPG refilling,fire extinguishers, emergency lighting.

```html
<!DOCTYPE html>
<html lang="en">
<head>
<meta charset="utf-8">
<title>Pembury Alarm Group – Fire and Building Compliance</title>
<link href="https://fonts.googleapis.com/css2?family=Ubuntu:wght@400;500;700&family=Open+Sans:wght@400;600;700&display=swap" rel="stylesheet">
<style>
:root{
  --orange:#fbaa00;
  --orange-dark:#f08a00;
  --orange-text:#f5a300;
  --ink:#222;
  --text:#555;
  --muted:#999;
  --panel:#f5f5f5;
  --band:#ebebeb;
  --dark:#1d1d1d;
  --bar:#333;
  --white:#fff;
  --tag:#dedede;
}
*{margin:0;padding:0;box-sizing:border-box}
html,body{width:979px;height:1200px;overflow:hidden;background:var(--white)}
body{position:relative;font-family:"Open Sans",Tahoma,sans-serif;color:var(--text);font-size:12px}
.abs{position:absolute}
a{color:inherit}
h1,h2,h3,h4{font-weight:400}

/* header */
.header-bg{left:0;top:0;width:979px;height:160px;background:linear-gradient(#fff 0%,#fff 55%,#e9e9e9 100%)}
.brand{left:36px;top:62px}
.brand-name{font-family:"Ubuntu",sans-serif;font-weight:500;font-size:25px;line-height:30px;color:var(--ink)}
.brand-tag{font-family:"Ubuntu",sans-serif;font-size:9px;letter-spacing:1px;color:var(--muted);margin-top:4px}
.search{left:629px;top:35px;display:flex;align-items:center;gap:8px;font-size:11px;color:#444}
.search-input{width:163px;height:26px;border:1px solid #ddd;background:#fff;margin-left:8px}
.search-go{width:34px;height:24px;background:var(--orange);color:#fff;border-radius:3px;font-family:"Ubuntu",sans-serif;font-weight:700;font-size:13px;display:flex;align-items:center;justify-content:center}
.nav{left:332px;top:83px;width:609px;height:77px;background:var(--white);border-top:1px solid #e6e6e6}
.nav-item{top:39px;font-family:"Ubuntu",sans-serif;font-weight:500;font-size:16px;color:var(--ink)}
.nav-item::before{content:"";position:absolute;left:50%;top:-47px;margin-left:-4px;border:4px solid transparent;border-top:5px solid var(--orange)}

/* hero */
.hero-band{left:0;top:160px;width:979px;height:411px;background:var(--band)}
.hero-photo{left:38px;top:173px;width:617px;height:385px;background:linear-gradient(180deg,#3d4a2c 0%,#56653f 22%,#6e6e69 40%,#5a5a58 70%,#3e3e3c 100%)}
.feature{left:655px;width:286px;background:linear-gradient(#fbb000,#f6a100);padding:20px 0 0 23px;color:#fff}
.feature h2{font-family:"Ubuntu",sans-serif;font-weight:700;font-size:27px;line-height:26px;letter-spacing:.5px}
.feature p{font-size:10px;color:#ffe6a6;text-transform:uppercase;line-height:12px}
.feature .more{display:flex;align-items:center;gap:5px;margin-top:9px;font-size:11px;color:#5a3b00}
.feature .dot{width:10px;height:10px;background:repeating-linear-gradient(90deg,#ffd66b 0 2px,transparent 2px 4px)}
.feature .dot.on{background:repeating-linear-gradient(90deg,#fff 0 2px,#c7c7c7 2px 4px)}
.tour{left:529px;top:490px;width:412px;height:68px;background:var(--bar)}
.tour-text{left:149px;top:20px;font-family:"Ubuntu",sans-serif;font-size:23px;color:#fff}
.tour-text b{color:var(--orange);font-weight:700}

/* section heads */
.sec-title{font-family:"Ubuntu",sans-serif;font-weight:400;font-size:28px;line-height:30px;color:#777;letter-spacing:-.3px}
.sec-title b{color:var(--orange);font-weight:700}
.sec-sub{font-size:10.5px;color:#b5b5b5;text-transform:uppercase}

/* welcome */
.welcome-photo{left:66px;top:668px;width:163px;height:94px;border:1px solid #ccc;padding:3px;background:#fff}
.welcome-photo div{width:100%;height:100%;background:linear-gradient(#3f5a2c,#6b7d52 50%,#6f6f6d)}
.welcome-text{left:246px;top:655px;width:375px;font-size:13px;line-height:18px;color:#555}
.welcome-text b{color:var(--orange-text);font-weight:700}
.link-list{left:72px;top:778px;list-style:none;font-size:11.5px;line-height:28px;color:#555}
.link-list li::before{content:"»";margin-right:14px;color:#777}
.link-list a{text-decoration:underline}

/* news */
.news-item{left:660px;top:652px;width:260px}
.news-head{display:flex;align-items:center;gap:12px;font-weight:700;color:var(--orange-text);font-size:13px}
.news-body{font-size:11.5px;line-height:18px;color:#222;text-decoration:underline;margin-top:10px}
.news-more{left:840px;top:719px;font-size:11px;color:var(--orange-text);display:flex;align-items:center;gap:6px}
.news-more span{width:13px;height:13px;border-radius:50%;background:#333;color:#fff;font-size:8px;display:flex;align-items:center;justify-content:center}
.tags-title{left:657px;top:736px;font-size:16px;color:#555}
.tags{left:657px;top:768px;width:260px;display:flex;flex-wrap:wrap;gap:7px 6px}
.tag{background:var(--tag);color:#666;font-size:9px;padding:7px 9px;border-radius:2px}
.tag.active{background:#555;color:#fff}

/* services */
.services{left:38px;top:874px;width:903px;height:238px;background:var(--panel)}
.svc-head{top:0;width:241px;height:46px;background:var(--dark);color:#aaa;font-family:"Ubuntu",sans-serif;font-weight:400;font-size:19px;padding:13px 0 0 36px}
.svc-head b{color:#fff;font-weight:700}
.svc-icon{top:60px;width:56px;height:56px}
.svc-link{top:78px;font-size:11.5px;line-height:18px;color:#222;text-decoration:underline}
.svc-title{top:138px;font-weight:700;font-size:13px;color:var(--orange-text)}
.svc-body{top:156px;width:230px;font-size:11.5px;line-height:18px;color:#555}

/* footer */
.footer-rule{left:38px;top:1113px;width:903px;height:4px;background:var(--bar)}
.footer-nav{left:0;top:1136px;width:979px;text-align:center;font-size:12px;color:#555}
.copyright{left:0;top:1159px;width:979px;text-align:center;font-size:10.5px;color:#666}
</style>
</head>
<body>

<header>
  <div class="abs header-bg"></div>
  <div class="abs brand">
    <div class="brand-name">Pembury Alarm Group</div>
    <div class="brand-tag">FIRE AND BUILDING COMPLIANCE</div>
  </div>
  <form class="abs search">Search the site<span class="search-input"></span><span class="search-go">GO</span></form>
  <nav class="abs nav">
    <a class="abs nav-item" style="left:38px">HOME</a>
    <a class="abs nav-item" style="left:134px">ABOUT</a>
    <a class="abs nav-item" style="left:240px">SERVICES</a>
    <a class="abs nav-item" style="left:359px">PRODUCTS</a>
    <a class="abs nav-item" style="left:495px">CONTACTS</a>
  </nav>
</header>

<section class="hero">
  <div class="abs hero-band"></div>
  <div class="abs hero-photo" role="img" aria-label="Photo of a fire extinguisher training unit burning on a car park with a gas cylinder beside it"></div>
  <div class="abs feature" style="top:173px;height:110px">
    <h2>FINANCE</h2><p>Lorem ipsum dolor sit amet, lorem</p>
    <div class="more"><span class="dot"></span><span class="dot"></span><span class="dot"></span>&nbsp;READ MORE</div>
  </div>
  <div class="abs feature" style="top:284px;height:102px;padding-top:15px">
    <h2>GLOBALIZATION</h2><p>Quisque ut magna et nisi</p>
    <div class="more"><span class="dot on"></span><span class="dot"></span><span class="dot on"></span>&nbsp;READ MORE</div>
  </div>
  <div class="abs feature" style="top:386px;height:104px;padding-top:15px">
    <h2>INNOVATION</h2><p>Lorem ipsum dolor sit amet, lorem</p>
    <div class="more"><span class="dot"></span><span class="dot"></span><span class="dot"></span>&nbsp;READ MORE</div>
  </div>
  <div class="abs tour">
    <svg class="abs" style="left:0;top:0" width="120" height="68" viewBox="0 0 120 68">
      <polygon points="0,0 40,0 74,34 40,68 0,68 34,34" fill="#2a2a2a"/>
      <polygon points="40,0 72,0 106,34 72,68 40,68 74,34" fill="#3b3b3b"/>
    </svg>
    <div class="abs tour-text"><b>START</b>TOUR NOW</div>
  </div>
</section>

<section class="welcome">
  <svg class="abs" style="left:58px;top:595px" width="44" height="44" viewBox="0 0 44 44">
    <rect x="1" y="1" width="42" height="42" rx="6" fill="#6a6a6a" stroke="#cfcfcf" stroke-width="2"/>
    <path d="M11 22 L19 30 L34 12" fill="none" stroke="#fff" stroke-width="5" stroke-linecap="round" stroke-linejoin="round"/>
  </svg>
  <div class="abs" style="left:109px;top:598px">
    <h1 class="sec-title"><b>WELCOME</b>TO OUR COMPANY!</h1>
    <div class="sec-sub">Lorem ipsum dolor sit amet, lorem</div>
  </div>
  <div class="abs welcome-photo"><div role="img" aria-label="Photo of staff demonstrating fire extinguisher use outdoors"></div></div>
  <p class="abs welcome-text"><b>Pembury Alarm Group</b> is a locally owned and operated fire protection company. Since 1978 we have evolved and developed to suit the demands of our clients and the 1992 Building Compliance Act. This ability to alter and change as required means that we are now viewed as an innovative and contemporary company.</p>
  <ul class="abs link-list">
    <li><a>Nam eu nulla. Donec lobortis purus vel urna. Nunc laoreet lacinia nunc. In volutpat sodales</a></li>
    <li><a>ipsum. Sed vestibulum. Integer in ante. Sed posuere ligula rhoncus erat. Fusce urna dui,</a></li>
    <li><a>sollicitudin ac, pulvinar quis, tincidunt et, risus. Quisque a nunc eget nibh interdum fringilla.</a></li>
  </ul>
</section>

<aside class="news">
  <svg class="abs" style="left:658px;top:595px" width="44" height="44" viewBox="0 0 44 44">
    <rect x="1" y="1" width="42" height="42" rx="6" fill="#6a6a6a" stroke="#cfcfcf" stroke-width="2"/>
    <path d="M11 22 L19 30 L34 12" fill="none" stroke="#fff" stroke-width="5" stroke-linecap="round" stroke-linejoin="round"/>
  </svg>
  <div class="abs" style="left:709px;top:598px">
    <h2 class="sec-title"><b>NEWS</b>UPDATES</h2>
    <div class="sec-sub">Lorem ipsum sit amet, lorem</div>
  </div>
  <div class="abs news-item">
    <div class="news-head">
      <svg width="16" height="18" viewBox="0 0 16 18"><rect x="1" y="3" width="14" height="14" rx="1" fill="#fff" stroke="#6a8fc2"/><rect x="1" y="3" width="14" height="4" fill="#6a8fc2"/><rect x="4" y="10" width="3" height="2" fill="#f5a300"/><rect x="9" y="10" width="3" height="2" fill="#bbb"/></svg>
      Duis tempor ipsum vitae diam.
    </div>
    <p class="news-body">Morbi volutpat leo in ligula. Integer vel magna. Quisque ut magna et nisi</p>
  </div>
  <div class="abs news-more">more <span>▶</span></div>
  <h3 class="abs tags-title">Tags</h3>
  <div class="abs tags">
    <span class="tag">Wanganui</span><span class="tag active">Fire Alarm</span><span class="tag">Building Compliance</span>
    <span class="tag">Building Warrant of Fitness</span><span class="tag">Fire Extinguishers</span>
    <span class="tag">Burglar Alarm Systems</span><span class="tag">LPG Refilling</span><span class="tag">BWOF</span>
  </div>
</aside>

<section class="abs services">
  <h3 class="abs svc-head" style="left:0"><b>FIRE</b> ALARMS</h3>
  <h3 class="abs svc-head" style="left:312px"><b>FIRE TECH</b> TRAINING</h3>
  <h3 class="abs svc-head" style="left:619px"><b>SALE</b> SERVICES?</h3>

  <svg class="abs svc-icon" style="left:12px" viewBox="0 0 56 56">
    <ellipse cx="22" cy="22" rx="18" ry="14" fill="#3f9ee6"/><polygon points="12,32 8,44 22,34" fill="#3f9ee6"/>
    <ellipse cx="36" cy="30" rx="15" ry="12" fill="#7fc94b"/><polygon points="44,38 50,48 38,40" fill="#7fc94b"/>
  </svg>
  <svg class="abs svc-icon" style="left:318px" viewBox="0 0 56 56">
    <g fill="#b8b8b8"><circle cx="28" cy="28" r="17"/>
    <rect x="24" y="4" width="8" height="48"/><rect x="4" y="24" width="48" height="8"/>
    <rect x="24" y="4" width="8" height="48" transform="rotate(45 28 28)"/><rect x="24" y="4" width="8" height="48" transform="rotate(-45 28 28)"/></g>
    <circle cx="28" cy="28" r="7" fill="#f5f5f5"/>
  </svg>
  <svg class="abs svc-icon" style="left:630px" viewBox="0 0 56 56">
    <circle cx="28" cy="28" r="25" fill="#e6e6e6" stroke="#bdbdbd" stroke-width="2"/><circle cx="28" cy="28" r="20" fill="#fff"/>
    <path d="M28 28 L28 13 M28 28 L38 34" stroke="#666" stroke-width="2" stroke-linecap="round"/><path d="M28 28 L18 22" stroke="#d33" stroke-width="1"/>
  </svg>

  <a class="abs svc-link" style="left:91px">Inter vel magna, sagittis.<br>Fusce elit ligula</a>
  <a class="abs svc-link" style="left:405px">Inter vel magna, sagittis.<br>Fusce elit ligula</a>
  <a class="abs svc-link" style="left:711px">Inter vel magna, sagittis.<br>Fusce elit ligula</a>

  <h4 class="abs svc-title" style="left:21px">Fusce interdum. Maecenas</h4>
  <h4 class="abs svc-title" style="left:326px">Maecenas non orci lorem ipsum</h4>
  <h4 class="abs svc-title" style="left:632px">Fusce interdum. Maecenas</h4>

  <p class="abs svc-body" style="left:21px">Morbi volutpat leo in ligula. Inter vel magna, sagittis. Fusce elit ligula, Aenean. Sed laoreet.</p>
  <p class="abs svc-body" style="left:326px">Morbi volutpat leo in ligula. Inter vel magna, sagittis. Fusce elit ligula, Aenean. Sed laoreet.</p>
  <p class="abs svc-body" style="left:632px">Morbi volutpat leo in ligula. Inter vel magna, sagittis. Fusce elit ligula, Aenean. Sed laoreet.</p>
</section>

<footer>
  <div class="abs footer-rule"></div>
  <nav class="abs footer-nav">HOME &nbsp;|&nbsp; ABOUT &nbsp;|&nbsp; SERVICES &nbsp;|&nbsp; PRODUCTS &nbsp;|&nbsp; SPONSORSHIP&nbsp;|&nbsp; INFO &nbsp;|&nbsp; CONTACTS</nav>
  <p class="abs copyright">Copyright 2019 © Pembury Alarm Group (PAG)</p>
</footer>

</body>
</html>
```